Needed! Great Book Cover for New Ghost Story

I need an enticing cover (both e-book and print formats) for a new mystery/thriller about ghosts. This is more of a paranormal or psychological thriller, not horror. The title should be easily visible in thumbnail view.

The story: a man is found dead in a gutted building* and a ghost is blamed. The ghost is a miner from the 1930s and is tall, thin, wears a long tail jacket and stovepipe hat (think Cornelius Bramwell). I have in mind a corpse outline near the steps with a ghostly shadow looming, but I am open to all interpretations and ideas.
Other elements in the story: female reporter, snakes, mountains, a haunted hotel called The Heron, copper and gold. The murder weapon was a knife.

Title and author:
Hollow Lanterns by Marla Quent

*The book is set in the mountain town of Jerome, Arizona. Please consider incorporating my own photographs in the design. See attached files.

Target Market(s)

Pelorix customers looking for new books; book store browsers

Font styles to use
Serif
Sans Serif

Requirements
Must have
• Prominent title and author name in easy-to-read font
Nice to have
• My photo as background; subtle element of the colors of copper and/or gold

```html
<!DOCTYPE html>
<html lang="en">
<head>
<meta charset="utf-8">
<title>Hollow Lanterns — Print Cover Wrap</title>
<link rel="stylesheet" href="https://fonts.googleapis.com/css2?family=Cinzel:wght@600;700&family=Crimson+Text:wght@400&display=swap">
<style>
  :root {
    --stage: #f1f1f1;
    --cover-dark: #121a1c;
    --cover-mid: #1d292c;
    --title-red: #b3262b;
    --title-deep: #5e0f14;
    --author-white: #ecebe6;
    --body-text: #d8d8d2;
    --brick: #4a2a2c;
    --stone: #6b6e72;
    --mist: #8d9491;
  }
  * { margin: 0; padding: 0; box-sizing: border-box; }
  html, body {
    width: 1200px; height: 800px; overflow: hidden;
    background: var(--stage);
  }
  .cover-wrap {
    position: absolute; left: 80px; top: 30px;
    width: 1040px; height: 740px;
    display: flex;
    box-shadow: 0 10px 30px rgba(0,0,0,0.25);
  }
  .back-cover, .front-cover {
    position: relative; width: 500px; height: 740px;
    background: linear-gradient(180deg, var(--cover-mid) 0%, var(--cover-dark) 100%);
    overflow: hidden;
  }
  .spine {
    width: 40px; height: 740px;
    background: #0d1214;
    display: flex; align-items: center; justify-content: space-between;
    flex-direction: column; padding: 30px 0;
    writing-mode: vertical-rl;
  }
  .spine-title {
    font-family: 'Cinzel', serif; font-weight: 700; font-size: 17px;
    color: var(--title-red); letter-spacing: 1px;
  }
  .spine-author {
    font-family: 'Cinzel', serif; font-weight: 600; font-size: 15px;
    color: var(--author-white); letter-spacing: 1px;
  }
  /* Front */
  .front-photo {
    position: absolute; left: 0; top: 150px; width: 500px; height: 590px;
  }
  .book-title {
    position: absolute; top: 40px; left: 0; width: 100%;
    text-align: center;
    font-family: 'Cinzel', serif; font-weight: 700;
    line-height: 0.95;
    background: linear-gradient(180deg, #d8484c 0%, var(--title-red) 45%, var(--title-deep) 100%);
    -webkit-background-clip: text; background-clip: text; color: transparent;
    filter: drop-shadow(0 0 10px rgba(0,0,0,0.9));
  }
  .book-title .line-one { display: block; font-size: 66px; }
  .book-title .line-two { display: block; font-size: 58px; }
  .author-name {
    position: absolute; bottom: 38px; left: 0; width: 100%;
    text-align: center;
    font-family: 'Cinzel', serif; font-weight: 600; font-size: 50px;
    color: var(--author-white);
    text-shadow: 0 2px 8px rgba(0,0,0,0.9);
  }
  /* Back */
  .blurb {
    position: absolute; top: 30px; left: 30px; right: 30px;
    font-family: 'Crimson Text', serif; font-size: 15.5px; line-height: 1.48;
    color: var(--body-text); text-align: justify; hyphens: auto;
  }
  .blurb p + p { margin-top: 18px; }
  .back-photo {
    position: absolute; left: 0; bottom: 0; width: 500px; height: 300px;
  }
  .back-title {
    position: absolute; bottom: 90px; left: 0; width: 100%; text-align: center;
    font-family: 'Cinzel', serif; font-weight: 700; font-size: 38px; line-height: 0.95;
    color: var(--title-red); opacity: 0.75;
  }
</style>
</head>
<body>
  <div class="cover-wrap">
    <section class="back-cover">
      <div class="blurb">
        <p>Lorem ipsum dolor sit amet, consectetur adipiscing elit. In quis sapien mollis, rhoncus dui in, ullamcorper sem. Vivamus convallis hendrerit sagittis. Cum sociis natoque penatibus et magnis dis parturient montes, nascetur ridiculus mus. Curabitur volutpat, lectus consectetur fringilla scelerisque, turpis neque ullamcorper tortor, vel tristique ex purus sed eros. Nunc ut nibh vitae mi lacinia ullamcorper. Aliquam nisi sem, malesuada nec arcu nec, convallis accumsan arcu. Fusce a elit et.</p>
        <p>Morbi vel tortor sapien. Etiam a tempor ipsum. Mauris accumsan, arcu quis lacinia sollicitudin, nunc augue porttitor turpis, et elementum sapien velit non ipsum. Donec rhoncus, ipsum rhoncus venenatis maximus, nisl quam vulputate orci, sit amet ornare ipsum lectus ac nulla. Vestibulum ante ipsum primis in faucibus orci luctus et ultrices posuere cubilia Curae; Nullam leo leo, mattis eu massa eget, lobortis tristique lacus. Fusce enim ex, viverra at tristique aliquet, lobortis nec augue. Duis metus mauris, maximus vitae arcu et, vehicula congue tellus. Vestibulum ante ipsum primis in faucibus orci luctus et ultrices posuere cubilia Curae; Nunc vel blandit metus.</p>
      </div>
      <svg class="back-photo" viewBox="0 0 500 300" role="img" aria-label="Faded photograph of a brick wall and stone steps in a gutted building">
        <defs>
          <linearGradient id="backFade" x1="0" y1="0" x2="0" y2="1">
            <stop offset="0" stop-color="#1a2427" stop-opacity="0"/>
            <stop offset="0.4" stop-color="#3a2a2d" stop-opacity="0.7"/>
            <stop offset="1" stop-color="#5a5e60" stop-opacity="0.8"/>
          </linearGradient>
        </defs>
        <rect width="500" height="300" fill="url(#backFade)"/>
      </svg>
      <div class="back-title">Hollow<br>Lanterns</div>
    </section>

    <div class="spine">
      <span class="spine-title">Hollow Lanterns</span>
      <span class="spine-author">Marla Quent</span>
    </div>

    <section class="front-cover">
      <svg class="front-photo" viewBox="0 0 500 590" role="img" aria-label="Photograph of a gutted brick building with a shadowy ghostly figure in a doorway above a corpse outline near the steps">
        <defs>
          <linearGradient id="wallFade" x1="0" y1="0" x2="0" y2="1">
            <stop offset="0" stop-color="#1d292c" stop-opacity="0"/>
            <stop offset="0.2" stop-color="#3c3437" stop-opacity="0.8"/>
            <stop offset="0.7" stop-color="#4a2a2c"/>
            <stop offset="1" stop-color="#2a2224"/>
          </linearGradient>
          <radialGradient id="doorMist" cx="0.5" cy="0.4" r="0.6">
            <stop offset="0" stop-color="#8d9491" stop-opacity="0.7"/>
            <stop offset="0.6" stop-color="#2a3335" stop-opacity="0.9"/>
            <stop offset="1" stop-color="#111719"/>
          </radialGradient>
        </defs>
        <rect width="500" height="590" fill="url(#wallFade)"/>
        <rect x="95" y="70" width="240" height="440" fill="url(#doorMist)"/>
      </svg>
      <h1 class="book-title"><span class="line-one">Hollow</span><span class="line-two">Lanterns</span></h1>
      <p class="author-name">Marla Quent</p>
    </section>
  </div>
</body>
</html>
```